Professional, Attractive, Simple Website Needed!!

We completed the design for our logo.

We need a website built out around this.

Here are a couple samples of how we want ours formatted.

http://brvtawatt.com

http://www.brightmerlo.com/lp/free-quote?LeadSource=Search%20Engine&ProgramName=webfind&experience=qual&language=en&type=brd&gclid=Xq7LMnvrTPKDWQAbZeRFtoPLmNcGxJbYTUWoKdMvCeWsfRgHyZnXpLoKqwErTyUiOpAsDfGhJkLzXcVb_zxwQ

http://qmorel.co

Project Deadline Extended
Reason: Extending this deadline due to our delay in providing designers with content for each page. This is coming in next 24 hours.

Project Deadline Extended
Reason: Due to scheduling conflicts and extended travel delays related to Puerto Rico, the deadline has been extended. Your patience is greatly appreciated.

Project Deadline Extended
Reason: Travel and scheduling conflicts have made it impossible to give this project the thorough review it deserves, therefore I am extending the deadline. Thank you for your patience!

Target Market(s)

Home Owners who earn 60k + household annually

Industry/Entity Type

It Professional

Coding

Coded - Design and coding required

Number of Pages Required

5+ page

Font styles to use
Serif

Colors
34a7d8
9bcb3c

Requirements
Must have
• Simple
• Lead form Entry (Ability for visitor to enter Name, number and address for a quote)
• Sleek Design
• Professional
• Testimonials
• Use color Scheme of Design Logo Attached
Nice to have
• Video when site starts
• Like this
• https://www.clipvault.com/watch?v=Rk8TpQwZmNe&feature=clipv.lt
Should not have
• Should not include Commercial solar
• Should not include wind power

```html
<!DOCTYPE html>
<html lang="en">
<head>
<meta charset="utf-8">
<title>Sunvale Energy — Solar That Saves</title>
<link href="https://fonts.googleapis.com/css2?family=Montserrat:wght@500;600;700&family=Open+Sans:ital,wght@0,400;0,600;0,700;1,700&family=Open+Sans+Condensed:wght@700&display=swap" rel="stylesheet">
<style>
:root{
  --blue:#34a7d8;
  --blue-deep:#1f8fc6;
  --green:#9bcb3c;
  --ink:#1c1c1c;
  --white:#ffffff;
  --frame:#e6e6e6;
  --sky-top:#c9d9e6;
  --sky-low:#6f7e8a;
}
*{margin:0;padding:0;box-sizing:border-box}
html,body{width:1200px;height:2413px;overflow:hidden}
body{background:var(--frame);font-family:"Open Sans",Arial,sans-serif;color:var(--ink);position:relative}
.page{position:absolute;left:13px;top:0;width:1174px;height:2399px;background:var(--white);overflow:hidden}
.abs{position:absolute}

/* hero */
.hero{left:0;top:0;width:1174px;height:660px;border-top:5px solid var(--blue)}
.hero-photo{position:absolute;inset:0;background:linear-gradient(180deg,#dfe7ee 0%,#b9c5cf 30%,#8a949b 60%,#58605a 85%,#3f4a3a 100%)}
.brand{left:32px;top:60px;display:flex;align-items:center;gap:12px}
.brand-dot{width:46px;height:46px;border-radius:50%;border:5px solid var(--green)}
.brand-name{font-family:"Montserrat",Arial,sans-serif;font-weight:600;font-size:26px;color:var(--blue);line-height:1}
.contact-bar{right:30px;top:36px;display:flex;align-items:center;gap:26px;font-family:"Montserrat",Arial,sans-serif;font-weight:600;font-size:17px;color:#3a3a3a}
.contact-item{display:flex;align-items:center;gap:9px}
.socials{display:flex;gap:6px}
.social{width:28px;height:28px;border-radius:50%;border:2px solid #3a3a3a}
.nav{right:36px;top:108px;display:flex;gap:40px;font-family:"Montserrat",Arial,sans-serif;font-weight:600;font-size:14px;color:var(--blue-deep)}
.nav a{color:inherit;text-decoration:none;padding-bottom:7px}
.nav a.active{color:var(--green);border-bottom:3px solid var(--green)}
.hero-panel{left:164px;top:290px;width:844px;height:249px;background:rgba(255,255,255,.28);border-radius:6px;padding:10px}
.hero-box{width:100%;height:100%;background:rgba(52,167,216,.86);border-radius:4px;text-align:center;color:var(--white);padding-top:30px}
.hero-title{font-family:"Montserrat",Arial,sans-serif;font-weight:600;font-size:38px;letter-spacing:1px}
.hero-copy{font-family:"Montserrat",Arial,sans-serif;font-weight:600;font-size:14px;line-height:18px;width:760px;margin:6px auto 0}
.quote-bar{width:506px;height:60px;margin:20px auto 0;background:var(--green);border-radius:4px;display:flex;align-items:center;gap:10px;padding:0 13px}
.zip{width:200px;height:36px;background:var(--white);border-radius:4px;color:var(--ink);font-family:"Montserrat",Arial,sans-serif;font-weight:600;font-size:15px;line-height:36px}
.calc{flex:1;height:36px;background:#0b0b0b;border-radius:4px;color:var(--white);font-family:"Montserrat",Arial,sans-serif;font-weight:600;font-size:15px;line-height:36px}

/* section headings */
.section-title{left:0;width:1174px;display:flex;justify-content:center;align-items:center;gap:14px;font-family:"Montserrat",Arial,sans-serif;font-weight:600;font-size:22px;letter-spacing:1px;color:var(--white)}
.section-title .rule{width:48px;height:2px;background:rgba(255,255,255,.8)}
.section-title .mark{width:34px;height:34px;border-radius:50%;border:3px solid var(--white)}

/* reviews */
.reviews{left:0;top:660px;width:1174px;height:405px;background:var(--green)}
.review{width:325px;height:177px;border:2px solid rgba(255,255,255,.85);border-radius:6px;top:128px}
.review::after{content:"";position:absolute;left:30px;bottom:-12px;width:20px;height:20px;background:var(--green);border-right:2px solid rgba(255,255,255,.85);border-bottom:2px solid rgba(255,255,255,.85);transform:rotate(45deg)}
.review-text{position:absolute;left:54px;top:22px;width:248px;font-size:13.5px;line-height:18px;color:var(--white)}
.qmark{position:absolute;font-family:Georgia,serif;font-weight:700;font-size:52px;line-height:1;color:var(--white)}
.qmark.open{left:16px;top:14px}
.qmark.close{left:158px;top:100px}
.portrait{position:absolute;width:96px;height:96px;border-radius:50%;border:4px solid var(--white);background:linear-gradient(160deg,#f2ede8,#c9b8a6 60%,#6c6f78);right:14px;top:128px;z-index:1}
.reviewer{position:absolute;left:0;top:322px;font-weight:700;font-style:italic;font-size:17px;color:var(--ink)}

/* faq */
.faqs{left:0;top:1065px;width:1174px;height:567px}
.faq-photo{position:absolute;inset:0;background:linear-gradient(180deg,#6db6df 0%,#4aa3d6 35%,#2f86c2 65%,#1e6fb0 100%)}
.faq-list{left:296px;top:128px;width:582px}
.faq{background:var(--white);border-radius:14px;height:38px;margin-bottom:8px;padding:0 16px;display:flex;justify-content:space-between;align-items:center;font-weight:700;font-size:15px}
.faq.open{display:block;height:201px;padding-top:9px}
.faq.open .faq-head{display:flex;justify-content:space-between;align-items:center}
.faq-body{font-size:13.5px;line-height:21px;font-weight:400;margin-top:4px;color:#333}

/* contact */
.contact{left:0;top:1632px;width:1174px;height:434px;background:var(--green)}
.field{background:var(--white);border:1px solid #cfd8c0;border-radius:3px;height:46px;top:129px;width:315px;padding:12px 15px;font-weight:700;font-size:15px}
.field.message{left:101px;top:188px;width:971px;height:137px}
.send{left:485px;top:336px;width:203px;height:42px;border-radius:6px;background:linear-gradient(180deg,#5b5b5b 0%,#1e1e1e 50%,#0a0a0a 100%);border:2px solid #cfcfcf;color:var(--white);text-align:center;line-height:38px;font-family:"Open Sans Condensed","Open Sans",Arial,sans-serif;font-weight:700;font-size:15px}

/* footer */
.footer-brand{left:0;width:1174px;top:2150px;display:flex;justify-content:center;align-items:center;gap:14px}
.footer-brand .brand-dot{width:60px;height:60px;border-width:6px}
.footer-brand .brand-name{font-size:30px}
.footer-nav{left:0;width:1174px;top:2290px;display:flex;justify-content:center;gap:44px;font-family:"Montserrat",Arial,sans-serif;font-weight:600;font-size:14px;color:var(--blue-deep)}
.footer-nav a{color:inherit;text-decoration:none;padding-bottom:7px}
.footer-nav a.active{color:var(--green);border-bottom:3px solid var(--green)}
.copyright{left:0;top:2360px;width:1174px;height:39px;background:var(--blue-deep);color:var(--white);text-align:center;line-height:39px;font-family:"Montserrat",Arial,sans-serif;font-weight:600;font-size:11px}
</style>
</head>
<body>
<div class="page">

  <header class="hero abs">
    <div class="hero-photo" role="img" aria-label="Street of modern terraced houses with solar panels on the roofs"></div>

    <div class="brand abs">
      <span class="brand-dot"></span>
      <span class="brand-name">SUNVALE ENERGY</span>
    </div>

    <div class="contact-bar abs">
      <span class="contact-item">
        <svg width="26" height="26" viewBox="0 0 26 26"><circle cx="13" cy="13" r="12" fill="none" stroke="#3a3a3a" stroke-width="2"/><path d="M9 7c1 0 2 2 2 3s-1 1-1 2 3 4 4 4 1-1 2-1 3 1 3 2-1 2-2 2c-4 0-10-6-10-10 0-1 1-2 2-2z" fill="#3a3a3a"/></svg>
        800-555-0148
      </span>
      <span class="contact-item">
        <svg width="26" height="26" viewBox="0 0 26 26"><circle cx="13" cy="13" r="12" fill="none" stroke="#3a3a3a" stroke-width="2"/><rect x="7" y="9" width="12" height="9" fill="none" stroke="#3a3a3a" stroke-width="1.6"/><path d="M7 9l6 5 6-5" fill="none" stroke="#3a3a3a" stroke-width="1.6"/></svg>
        info@sunvaleenergy.com
      </span>
      <span class="socials"><span class="social"></span><span class="social"></span></span>
    </div>

    <nav class="nav abs">
      <a class="active" href="#">HOME</a><a href="#">REVIEWS</a><a href="#">FAQs</a><a href="#">CONTACT</a>
    </nav>

    <div class="hero-panel abs">
      <div class="hero-box">
        <h1 class="hero-title">SOLAR THAT SAVES</h1>
        <p class="hero-copy">Our solar panels not only generate energy for your home, they can also generate cash in your pocket. That's because when you go solar you can save on your monthly utility bill. The savings over time add up and allow you to plan for your future.</p>
        <div class="quote-bar">
          <div class="zip">ENTER ZIP CODE</div>
          <div class="calc">CALCULATE YOUR SAVINGS</div>
        </div>
      </div>
    </div>
  </header>

  <section class="reviews abs">
    <h2 class="section-title abs" style="top:56px"><span class="rule"></span><span class="mark"></span>REVIEWS<span class="rule"></span></h2>

    <div class="review abs" style="left:75px">
      <span class="qmark open">&#8221;</span>
      <p class="review-text">Lorem ipsum dolor sit amet, consectetu er adipiscing elit, sed diam nonummy nibh euismod tincidunt ut laoreet dolor magna aliquam erat volu. Wisi enim ad minim veniam.</p>
      <span class="qmark close">&#8221;</span>
      <span class="portrait" role="img" aria-label="Customer portrait" style="top:120px;right:14px"></span>
      <span class="reviewer">Marla Jennings</span>
    </div>
    <div class="review abs" style="left:426px">
      <span class="qmark open">&#8221;</span>
      <p class="review-text">Lorem ipsum dolor sit amet, consectetu er adipiscing elit, sed diam nonummy nibh euismod tincidunt ut laoreet dolor magna aliquam erat volu. Wisi enim ad minim veniam.</p>
      <span class="qmark close">&#8221;</span>
      <span class="portrait" role="img" aria-label="Customer portrait" style="top:120px;right:14px"></span>
      <span class="reviewer">Renee Talbot</span>
    </div>
    <div class="review abs" style="left:775px">
      <span class="qmark open">&#8221;</span>
      <p class="review-text">Lorem ipsum dolor sit amet, consectetu er adipiscing elit, sed diam nonummy nibh euismod tincidunt ut laoreet dolor magna aliquam erat volu. Wisi enim ad minim veniam.</p>
      <span class="qmark close">&#8221;</span>
      <span class="portrait" role="img" aria-label="Customer portrait" style="top:120px;right:14px"></span>
      <span class="reviewer">Derek Colston</span>
    </div>
  </section>

  <section class="faqs abs">
    <div class="faq-photo" role="img" aria-label="Blurred house with rows of blue solar panels"></div>
    <h2 class="section-title abs" style="top:56px"><span class="rule"></span><span class="mark"></span>FAQS<span class="rule"></span></h2>

    <div class="faq-list abs">
      <div class="faq">Question 1<svg width="12" height="8" viewBox="0 0 12 8"><path d="M1 1l5 5 5-5" fill="none" stroke="#222" stroke-width="2"/></svg></div>
      <div class="faq open">
        <div class="faq-head">Question 2<svg width="12" height="8" viewBox="0 0 12 8"><path d="M1 7l5-5 5 5" fill="none" stroke="#222" stroke-width="2"/></svg></div>
        <p class="faq-body">Lorem ipsum dolor sit amet, consectetuer adipiscing elit, sed diam nonummy nibh euismod tincidunt ut laoreet dolore magna aliquam erat volutpat. Ut wisi enim ad minim veniam, quis nostrud exerci tation ullamcorper suscipit lobortis nisl ut aliquip ex ea commodo consequat. Duis autem vel eum iriure dolor in hendrerit in vulputate velit esse molestie consequat, vel illum dolore eu feugiat nulla facilisis at vero eros et accumsan et iusto odio dignissim qui blandit praesent luptatum zzril delenit augue duis dolore te feugait nulla facilisi.</p>
      </div>
      <div class="faq">Question 3<svg width="12" height="8" viewBox="0 0 12 8"><path d="M1 1l5 5 5-5" fill="none" stroke="#222" stroke-width="2"/></svg></div>
      <div class="faq">Question 4<svg width="12" height="8" viewBox="0 0 12 8"><path d="M1 1l5 5 5-5" fill="none" stroke="#222" stroke-width="2"/></svg></div>
      <div class="faq">Question 5<svg width="12" height="8" viewBox="0 0 12 8"><path d="M1 1l5 5 5-5" fill="none" stroke="#222" stroke-width="2"/></svg></div>
    </div>
  </section>

  <section class="contact abs">
    <h2 class="section-title abs" style="top:56px"><span class="rule"></span><span class="mark"></span>CONTACT<span class="rule"></span></h2>
    <div class="field abs" style="left:101px">Your Name</div>
    <div class="field abs" style="left:429px">Your Email</div>
    <div class="field abs" style="left:757px">Your Subject</div>
    <div class="field message abs">Message</div>
    <div class="send abs">SEND MESSAGE</div>
  </section>

  <footer>
    <div class="footer-brand abs">
      <span class="brand-dot"></span>
      <span class="brand-name">SUNVALE ENERGY</span>
    </div>
    <nav class="footer-nav abs">
      <a class="active" href="#">HOME</a><a href="#">REVIEWS</a><a href="#">FAQs</a><a href="#">CONTACT</a>
    </nav>
    <div class="copyright abs">COPYRIGHT © 2017 SUNVALE ENERGY. ALL RIGHTS RESERVED.</div>
  </footer>

</div>
</body>
</html>
```